Business Card design for insurance broker in Denver, CO, USA

I need a business card designed using this logo that was just created. We sell life and disability income insurance to US consumers.
Looking for a professionally designed card to make use of the logo and have something to hand to prospects or new business referral sources. The card could be white, gray, black or whatever you would recommend.

Target Market(s)

US Consumers and other financial professionals that I partner with.

Industry/Entity Type

Insurance Broker

Contact Information for Business Card

Owen R. Tessler, CLU, LUTCF (please note that CLU should have a superscript R in a circle for registered trademark)
President
phone (303) 555-0147
email owen@brightlakecoverage.com
4620 W. Hollister Rd, Suite 310, Cedar Ridge, CO 80199
Somewhere fit in a tagline saying "Your resource for life, long term care, and disability insurance" (maybe the back if it doesn't fit on the front, your call)

Font styles to use
Sans Serif

Requirements
Must have
• Must have logo in correct blue and gray colors, my name, address, phone, email. Order and placement determined by the designer.
• I just want something that looks a more professional than what I could have done using the business card designer tool on printmakerhub.com or CardNest, or any other do-it-yourself tool
• A regular rectangular business card with square corners is preferred
Nice to have
• I included the logos of 2 organizations I belong to (GQLF and BEPWO). They should be small, but visible on the back only. If it doesn’t look good, this is not a requirement, feel free to drop it.
Should not have
• Do not add any colors not already in the logo, except use of black and whites which are okay. If you use the logo on the back and want to make that in all black, gray or white, that may be okay as well.

```html
<!DOCTYPE html>
<html lang="en">
<head>
<meta charset="utf-8">
<title>Brightlake Coverage — Business Card</title>
<link rel="stylesheet" href="https://fonts.googleapis.com/css2?family=Lato:wght@400;700&display=swap">
<style>
  :root {
    --backdrop: #9a9a9a;
    --card-dark: #2b2b2b;
    --card-light: #ffffff;
    --band-gray: #a7a7a7;
    --brand-blue: #1f7fcc;
    --brand-gray: #8c8c8c;
    --text-gray: #9b9b9b;
    --white: #ffffff;
  }
  * { box-sizing: border-box; margin: 0; padding: 0; }
  html, body { width: 1200px; height: 930px; overflow: hidden; }
  body {
    background: var(--backdrop);
    font-family: "Lato", Arial, sans-serif;
    position: relative;
  }
  .card {
    position: absolute;
    width: 620px;
    height: 354px;
    border-radius: 18px;
    overflow: hidden;
    box-shadow: 0 6px 18px rgba(0,0,0,0.25);
  }
  /* Back */
  .card-back { left: 60px; top: 60px; background: var(--card-dark); }
  .card-back .brand {
    position: absolute; left: 0; right: 0; top: 130px;
    display: flex; align-items: center; justify-content: center; gap: 16px;
  }
  .brand-mark {
    flex: none;
    width: 58px; height: 58px; border-radius: 50%;
    border: 4px solid var(--brand-blue);
  }
  .brand-name {
    font-weight: 700; color: var(--brand-blue);
    font-size: 34px; letter-spacing: 1px; line-height: 1; white-space: nowrap;
  }
  .tagline {
    position: absolute; left: 0; right: 0; bottom: 28px;
    text-align: center; color: var(--white);
    font-size: 13px; letter-spacing: 0.5px; text-transform: uppercase;
  }
  /* Front */
  .card-front { left: 520px; top: 516px; background: var(--card-light); }
  .side-band {
    position: absolute; left: 0; top: 0; bottom: 0; width: 100px;
    background: var(--band-gray);
  }
  .card-front .brand {
    position: absolute; left: 52px; top: 40px;
    display: flex; align-items: center; gap: 18px;
  }
  .card-front .brand-mark {
    width: 96px; height: 96px; background: var(--white); border-width: 5px;
  }
  .card-front .brand-name { font-size: 30px; }
  .contact { position: absolute; left: 150px; top: 160px; color: var(--text-gray); }
  .contact .name { color: var(--brand-blue); font-size: 21px; font-weight: 700; white-space: nowrap; }
  .contact .name sup { font-size: 11px; }
  .contact .role { font-size: 17px; margin-bottom: 14px; }
  .contact .address { font-size: 16px; line-height: 1.3; margin-bottom: 12px; }
  .contact .line { display: flex; align-items: center; gap: 10px; font-size: 16px; line-height: 1.5; }
  .contact svg { width: 14px; height: 14px; fill: none; stroke: var(--brand-blue); stroke-width: 2; }
  .badges {
    position: absolute; right: 34px; top: 150px;
    display: flex; align-items: center; gap: 22px;
  }
  .badge-round { width: 50px; height: 50px; border-radius: 50%; background: var(--brand-blue); }
  .badge-square { width: 44px; height: 44px; background: var(--brand-gray); }
</style>
</head>
<body>
  <section class="card card-back">
    <div class="brand">
      <span class="brand-mark"></span>
      <span class="brand-name">BRIGHTLAKE COVERAGE</span>
    </div>
    <p class="tagline">Your resource for life, long term care, and disability insurance</p>
  </section>

  <section class="card card-front">
    <div class="side-band"></div>
    <div class="brand">
      <span class="brand-mark"></span>
      <span class="brand-name">BRIGHTLAKE COVERAGE</span>
    </div>
    <div class="contact">
      <p class="name">Owen R. Tessler, CLU<sup>®</sup>, LUTCF</p>
      <p class="role">President</p>
      <p class="address">4620 W. Hollister Rd, Suite 310,<br>Cedar Ridge, CO 80199</p>
      <p class="line">
        <svg viewBox="0 0 16 16"><path d="M3 2l3 0 1 3-2 1.5c1 2 2.5 3.5 4.5 4.5L11 9l3 1v3c-6 0-11-5-11-11z"/></svg>
        (303) 555-0147
      </p>
      <p class="line">
        <svg viewBox="0 0 16 16"><rect x="1.5" y="3.5" width="13" height="9"/><path d="M1.5 3.5l6.5 5 6.5-5"/></svg>
        owen@brightlakecoverage.com
      </p>
    </div>
    <div class="badges">
      <span class="badge-square" role="img" aria-label="Member association badge"></span>
      <span class="badge-round" role="img" aria-label="Professional roundtable badge"></span>
    </div>
  </section>
</body>
</html>
```